Re-design of 4 x 2-sided reports

I need the 4 attached reports (3 are 2-sides of A4; 1 is 7-sides of A4) to be re-designed with a consistent look and feel. Just need 1 or 2 images per report being inserted plus consistent branding and contact details being displayed in the same location on each report with same colour, font and design). Reports are attached.
The reports are used as lead magnets.
That is, visitors to our website can download one of them (7 Steps To Sharpen Your Sales Over The Coming Month) by filling in a form with their email address. Then over the next 30 days the other reports are sent to the subscriber via email autoresponders.
Blue Harbour Marketing is a marketing consultancy dealing with companies in the North West of England providing cost-effective and profitable marketing to small and medium-sized businesses that want better and quicker results. The reports need to be professional and corporate looking. Please let me know if you need any further clarification or have any questions. I attach an example report. I don't necessarily want to mirror this report (from the law firm) but it may help to understand what look I'm trying to get. Many thanks, Gordon

Target Market(s)

SMEs based in NW of England
Typically with turnover of £1m to £10m or 10 to 100 employees
Clients often in the construction sector, healthcare, accountants, lawyers and local councils.

Industry/Entity Type

Marketing

Font styles to use
Serif
Sans Serif

Colors
ec1f27

Requirements
Must have
• Consistent branding
• Logo in same place across all four reports
• Contact details in same place across all four reports
• Same font across all four reports
• Same colour across all four reports
• Professional and bold look
Nice to have
• Some strong stock photography
• 1 or 2 images per report
• More images for the 7-page report though
Should not have
• No graphics

```html
<!DOCTYPE html>
<html lang="en">
<head>
<meta charset="utf-8">
<title>10 Quick &amp; Easy Ways To Grow Your Business Using Social Media – Blue Harbour Marketing</title>
<link href="https://fonts.googleapis.com/css2?family=Montserrat:wght@300;400;500;600&family=Open+Sans:wght@400;600&display=swap" rel="stylesheet">
<style>
  :root {
    --brand: #b5002a;
    --brand-dark: #7f1a27;
    --header-grey: #efefef;
    --ink: #222222;
    --paper: #ffffff;
    --backdrop: #e9e6e1;
    --network-blue: #0a66c2;
  }
  * { margin: 0; padding: 0; box-sizing: border-box; }
  html, body { width: 1200px; height: 1200px; overflow: hidden; background: var(--backdrop); }
  .page {
    position: absolute; left: 202px; top: 38px;
    width: 884px; height: 1250px;
    transform: scale(0.9); transform-origin: 0 0;
    background: var(--paper);
    box-shadow: 0 6px 18px rgba(0,0,0,.18);
    font-family: "Open Sans", Arial, sans-serif;
    color: var(--ink);
    overflow: hidden;
  }
  .masthead {
    position: absolute; left: 0; top: 0; width: 884px; height: 133px;
    background: var(--header-grey);
  }
  .brand {
    position: absolute; left: 50px; top: 28px; width: 300px;
    display: flex; align-items: center; gap: 12px;
  }
  .brand-square { flex: 0 0 auto; width: 60px; height: 74px; background: var(--brand); }
  .brand-name {
    font-family: "Montserrat", Arial, sans-serif; font-weight: 500;
    font-size: 29px; line-height: 34px; color: var(--brand);
  }
  .report-title {
    position: absolute; left: 416px; top: 33px; width: 420px;
    font-family: "Montserrat", Arial, sans-serif; font-weight: 600;
    font-size: 23.5px; line-height: 29px; color: var(--brand);
  }
  .title-rule {
    position: absolute; left: 416px; top: 105px; width: 417px; height: 2px; background: var(--brand);
  }
  .facts {
    position: absolute; font-size: 18px; line-height: 21.5px; list-style: none;
  }
  .facts li { position: relative; padding-left: 20px; }
  .facts li::before {
    content: "•"; position: absolute; left: 0; top: 0; font-size: 14px;
  }
  .facts li.continued::before { content: none; }
  .facts-left-top { left: 136px; top: 185px; width: 280px; }
  .facts-left-bottom { left: 136px; top: 421px; width: 280px; }
  .facts-right { left: 553px; top: 185px; width: 280px; }
  .network-badge {
    position: absolute; left: 50px; top: 422px;
    display: flex; align-items: center; gap: 6px;
  }
  .network-square { width: 16px; height: 16px; background: var(--network-blue); }
  .network-name { font-size: 15px; line-height: 20px; font-weight: 600; color: var(--network-blue); }
  .summary-band {
    position: absolute; left: 0; top: 553px; width: 884px; height: 545px;
    background: var(--brand); color: #ffffff;
  }
  .summary-heading {
    position: absolute; left: 50px; top: 50px;
    font-family: "Montserrat", Arial, sans-serif; font-weight: 600; font-size: 20px;
  }
  .summary-col { position: absolute; width: 372px; font-size: 18px; line-height: 21.5px; }
  .summary-col p + p { margin-top: 21.5px; }
  .summary-col-left { left: 50px; top: 98px; }
  .summary-col-right { left: 467px; top: 51px; }
  .summary-photo {
    position: absolute; left: 467px; top: 288px; width: 366px; height: 207px;
    background: linear-gradient(135deg, #3a3640 0%, #5a4a6a 30%, #2e4a78 60%, #2a2a2e 100%);
  }
  .footer {
    position: absolute; left: 0; top: 1148px; width: 884px; height: 102px;
    background: var(--brand-dark); color: #f3e6e8;
    font-family: "Montserrat", Arial, sans-serif; font-weight: 300;
    font-size: 18px; line-height: 22px; text-align: center;
    padding-top: 27px;
  }
</style>
</head>
<body>
  <article class="page">
    <header class="masthead">
      <div class="brand">
        <span class="brand-square"></span>
        <span class="brand-name">Blue Harbour<br>Marketing</span>
      </div>
      <h1 class="report-title">10 Quick &amp; Easy Ways To Grow Your Business Using Social Media</h1>
      <div class="title-rule"></div>
    </header>

    <ul class="facts facts-left-top">
      <li class="continued">reference to a product or brand</li>
      <li>50 million chirps sent a day worldwide</li>
      <li>Can be used to promote news, events, new appointments, new website, success, and defend criticism or complaints!</li>
      <li>More than 230 million users worldwide</li>
    </ul>

    <div class="network-badge">
      <span class="network-square"></span>
      <span class="network-name">ProLink</span>
    </div>
    <ul class="facts facts-left-bottom">
      <li>15 million users in the UK</li>
      <li>347 million users worldwide</li>
      <li>Free advertising of your services and expertise</li>
    </ul>

    <ul class="facts facts-right">
      <li>Ability to identify prospects</li>
      <li>Free to post jobs on site if you are hiring</li>
      <li>Is becoming part of the 'sifting' or selection process of companies wanting new suppliers</li>
      <li>Status Updates = free advertising</li>
      <li>Q &amp; As = show and 'advertise' your expertise</li>
    </ul>

    <section class="summary-band">
      <h2 class="summary-heading">Summary</h2>
      <div class="summary-col summary-col-left">
        <p>Social media is now used by millions of people (including many of your customers) both here in the UK and across the world.</p>
        <p>People use it to connect with other people but also to find products and services that they may need.</p>
        <p>Social media provides all businesses with a free, relatively easy way to promote their business to existing and potential new customers.</p>
        <p>Those that are embracing social media and investing some time and effort into learning how to get the most from social media are really helping to grow their businesses. For those businesses that haven't yet</p>
      </div>
      <div class="summary-col summary-col-right">
        <p>considered social media (for whatever reason) or are not taking full advantage of the benefits of social media, they are definitely missing an opportunity to grow their business and are 'leaving money on the table'.</p>
        <p>We believe it is, therefore, becoming imperative that virtually all businesses participate, to some degree, in social media.</p>
      </div>
      <div class="summary-photo" role="img" aria-label="Close-up photograph of a smartphone screen showing social media app icons"></div>
    </section>

    <footer class="footer">
      Copyright @ Blue Harbour Marketing<br>
      www.blueharbourmarketing.co.uk |01632 960 418 | info@blueharbourmarketing.co.uk
    </footer>
  </article>
</body>
</html>
```